Quote Cards With TK May 2025 for Instagram

I would like to put these quotes over one of the pictures attached; Instagram (new size: 4:5 (1080 x 1350 pixels) One Quote per picture, and I want the quote to be bold or easy to read as well. I provided a few reference graphics that I really like as examples below. In very small letters at the bottom add @TKBarlowOnline

All of the pictures are attached; you can pick any photo and add one quote to it; but no stock photography

```html
<!DOCTYPE html>
<html lang="en">
<head>
<meta charset="utf-8">
<title>Quote Cards With TK</title>
<link href="https://fonts.googleapis.com/css2?family=Abril+Fatface&family=Oswald:wght@600&family=Poppins:wght@400;500;600;700;800&family=Yellowtail&display=swap" rel="stylesheet">
<style>
  :root {
    --pink: #ff0a85;
    --pink-soft: #ff4da6;
    --pink-light: #ff7ec0;
    --ink: #141414;
    --paper: #ffffff;
    --backdrop: #c8c8c8;
    --edge: #6d6d6d;
  }
  * { margin: 0; padding: 0; box-sizing: border-box; }
  html, body { width: 983px; height: 1200px; overflow: hidden; background: var(--backdrop); }
  .board { position: relative; width: 983px; height: 1200px; }
  .card {
    position: absolute; width: 409px; height: 512px; background: var(--paper);
    outline: 1px solid var(--edge); overflow: hidden; font-family: "Poppins", sans-serif;
  }
  .card--tired { left: 55px; top: 72px; }
  .card--fault { left: 511px; top: 72px; }
  .card--hormonal { left: 55px; top: 631px; }
  .card--flat { left: 511px; top: 631px; }
  .abs { position: absolute; }
  .center { left: 0; right: 0; text-align: center; }
  .handle { font-size: 16.5px; color: var(--ink); font-weight: 400; }
  .handle--pink { color: var(--pink); }

  /* Card 1 */
  .tired__band { left: 0; top: 0; width: 100%; height: 235px; background: var(--pink); }
  .tired__title {
    top: 48px; font-family: "Abril Fatface", serif; color: var(--paper);
    font-size: 50px; line-height: 54px; text-shadow: 2px 2px 0 #b8005c;
  }
  .tired__pill {
    left: 30px; top: 179px; width: 345px; height: 102px; border-radius: 51px;
    background: var(--paper); border: 2px solid var(--pink);
    display: flex; align-items: center; justify-content: center;
  }
  .tired__pill-text { font-family: "Abril Fatface", serif; color: var(--pink); font-size: 76px; line-height: 1; margin-top: -6px; }
  .tired__sub { top: 300px; font-size: 27px; line-height: 35px; color: var(--ink); }
  .tired__fix {
    top: 390px; font-family: "Abril Fatface", serif; color: var(--pink);
    font-size: 46px; line-height: 50px; letter-spacing: -2px;
  }
  .card--tired .handle { left: 44px; top: 471px; }

  /* Card 2 */
  .fault__art { left: 0; top: 0; }
  .fault__that { left: 41px; top: 26px; color: var(--paper); font-weight: 700; font-size: 25px; line-height: 30px; letter-spacing: 1px; }
  .fault__weight {
    top: 60px; left: 0; width: 409px; text-align: center; padding-left: 6px; color: var(--paper);
    font-weight: 800; font-size: 30px; line-height: 36px; text-shadow: 2px 2px 0 #8a003f;
  }
  .fault__headline {
    top: 124px; font-family: "Abril Fatface", serif; color: var(--ink);
    font-size: 46px; line-height: 56px; letter-spacing: -1px;
  }
  .fault__blame {
    top: 217px; font-family: "Abril Fatface", serif; color: var(--paper);
    font-size: 41px; line-height: 50px;
  }
  .fault__alone { top: 368px; font-weight: 600; font-size: 24.5px; line-height: 32px; color: var(--ink); }
  .fault__fix {
    top: 398px; font-family: "Oswald", sans-serif; font-weight: 600; color: var(--pink);
    font-size: 50px; line-height: 64px; letter-spacing: -0.5px;
  }
  .card--fault .handle { right: 56px; top: 474px; }

  /* Card 3 */
  .hormonal__title {
    left: 36px; top: 46px; color: var(--pink); font-weight: 700;
    font-size: 62px; line-height: 68px; letter-spacing: -1.5px;
  }
  .hormonal__script {
    top: 187px; font-family: "Yellowtail", cursive; color: var(--ink);
    font-size: 66px; line-height: 80px;
  }
  .hormonal__banner { left: 33px; top: 284px; }
  .hormonal__banner-text {
    left: 52px; top: 284px; height: 57px; line-height: 57px; color: var(--paper);
    font-weight: 700; font-size: 21px; letter-spacing: -0.6px;
  }
  .hormonal__rule { left: 33px; top: 341px; width: 2px; height: 171px; background: var(--pink); }
  .hormonal__cta { left: 52px; top: 362px; font-weight: 600; font-size: 26px; line-height: 33px; color: var(--ink); }
  .card--hormonal .handle { right: 38px; top: 466px; }

  /* Card 4 */
  .flat__band { left: 0; top: 0; width: 100%; height: 276px; background: var(--pink); }
  .flat__title {
    left: 36px; top: 28px; color: var(--paper); font-weight: 700;
    font-size: 72px; line-height: 71px; letter-spacing: -1px;
  }
  .flat__possible { left: 36px; top: 296px; font-weight: 600; font-size: 37px; line-height: 48px; color: var(--ink); letter-spacing: -0.5px; }
  .flat__pill {
    left: 38px; top: 354px; width: 334px; height: 41px; border-radius: 12px; background: var(--pink);
    color: var(--paper); font-size: 26px; line-height: 41px; text-align: center; white-space: nowrap;
  }
  .flat__pill strong { font-weight: 700; margin-left: 6px; }
  .flat__note { left: 38px; top: 408px; font-weight: 500; font-size: 15.5px; line-height: 22px; color: var(--ink); }
  .card--flat .handle { left: 37px; top: 466px; }
</style>
</head>
<body>
<main class="board">

  <section class="card card--tired">
    <div class="abs tired__band"></div>
    <h2 class="abs center tired__title">Tired. Moody.<br>Stubborn.</h2>
    <div class="abs tired__pill"><span class="tired__pill-text">Belly Fat</span></div>
    <p class="abs center tired__sub">Your Hormones Are<br>Screaming For Help!</p>
    <p class="abs center tired__fix">LET’S FIX THAT.</p>
    <p class="abs handle">@TKBarlowOnline</p>
  </section>

  <section class="card card--fault">
    <svg class="abs fault__art" width="409" height="512" viewBox="0 0 409 512" aria-hidden="true">
      <defs>
        <linearGradient id="faultTop" x1="0" y1="0" x2="1" y2="1">
          <stop offset="0" stop-color="#ff62b0"/>
          <stop offset="0.5" stop-color="#ff1a8c"/>
          <stop offset="1" stop-color="#ff0a85"/>
        </linearGradient>
        <linearGradient id="faultMid" x1="0" y1="0" x2="1" y2="1">
          <stop offset="0" stop-color="#ff5aaa"/>
          <stop offset="0.6" stop-color="#ff0a85"/>
        </linearGradient>
      </defs>
      <rect x="0" y="0" width="409" height="114" fill="url(#faultTop)"/>
      <path d="M0 0 Q20 80 58 114 L0 114 Z" fill="#ff7ec0" opacity="0.7"/>
      <path d="M300 0 Q405 20 409 114 L409 0 Z" fill="#ff7ec0" opacity="0.5"/>
      <rect x="0" y="114" width="409" height="81" fill="#ffffff"/>
      <rect x="0" y="195" width="409" height="317" fill="url(#faultMid)"/>
      <path d="M0 195 L0 270 Q20 330 70 342 L35 342 L35 195 Z" fill="#ff7ec0" opacity="0.45"/>
      <line x1="35" y1="195" x2="35" y2="342" stroke="#ffffff" stroke-width="1.5"/>
      <line x1="372" y1="195" x2="372" y2="342" stroke="#ffffff" stroke-width="1.5"/>
      <path d="M0 512 L0 371 Q0 343 28 343 L381 343 Q409 343 409 371 L409 512 Z" fill="#ffffff"/>
    </svg>
    <p class="abs fault__that">THAT</p>
    <p class="abs fault__weight">STUBBORN WEIGHT?</p>
    <h2 class="abs center fault__headline">It’s not your fault</h2>
    <p class="abs center fault__blame">Your Hormones<br>Are To Blame</p>
    <p class="abs center fault__alone">AND YOU’RE NOT ALONE</p>
    <p class="abs center fault__fix">BUT THERE IS A FIX</p>
    <p class="abs handle handle--pink">@TKBarlowOnline</p>
  </section>

  <section class="card card--hormonal">
    <h2 class="abs hormonal__title">Your Belly<br>Isn’t Fat...</h2>
    <p class="abs center hormonal__script">It’s Hormonal</p>
    <svg class="abs hormonal__banner" width="356" height="57" viewBox="0 0 356 57" aria-hidden="true">
      <path d="M0 0 L336 0 L356 28.5 L336 57 L0 57 Z" fill="#ff0a85"/>
    </svg>
    <p class="abs hormonal__banner-text">AND HERE’S HOW TO FIX IT</p>
    <div class="abs hormonal__rule"></div>
    <p class="abs hormonal__cta">Comment HORMONES<br>if nothing is working</p>
    <p class="abs handle">@TKBarlowOnline</p>
  </section>

  <section class="card card--flat">
    <div class="abs flat__band"></div>
    <h2 class="abs flat__title">Flat<br>tummy in<br>your 40s?</h2>
    <p class="abs flat__possible">It’s still possible!</p>
    <p class="abs flat__pill">Comment<strong>BYE BELLY</strong></p>
    <p class="abs flat__note">To Get The 10 Secrets To A Flatter Tummy</p>
    <p class="abs handle handle--pink">@TKBarlowOnline</p>
  </section>

</main>
</body>
</html>
```